Film and TV production company

I have the logo already designed by mark quarry. I just need the text and the logo attached to the business card. Maybe a small design on the back of the card or text.

Industry/Entity Type

film tv arts

Contact Information for Business Card

Dale Morrow Cinematographer-Director

Colors
F0912C
F2A743
F7CA91
FBE8D2
FDF5EE
EE7325
F08F49
F5BC92
FAE3D3
FDF4ED

Requirements
Must have
• www.copperlanepix.com.au my email address mail@copperlanepix.com.au my mobile number 0491570158
Nice to have
• Some kind of small art work on the back that ties in with the logo design attached
Should not have
• Must clean and simple

```html
<!DOCTYPE html>
<html lang="en">
<head>
<meta charset="utf-8">
<title>Copper Lane Pictures – Business Card</title>
<link rel="stylesheet" href="https://fonts.googleapis.com/css2?family=Montserrat:wght@400;700&family=Poppins:wght@300;400&display=swap">
<style>
  :root {
    --stage: #3a3b3e;
    --orange: #e67e1a;
    --copper: #a8601a;
    --olive: #3f4f1c;
    --ink: #1d1d1d;
    --rule: #2a2a2a;
    --paper: #ffffff;
  }
  * { box-sizing: border-box; margin: 0; padding: 0; }
  html, body { width: 1200px; height: 801px; overflow: hidden; }
  body {
    background: var(--stage);
    position: relative;
    font-family: "Poppins", sans-serif;
  }
  .card {
    position: absolute;
    top: 246px;
    width: 540px;
    height: 309px;
    border-radius: 14px;
    overflow: hidden;
    box-shadow: 0 10px 28px rgba(0,0,0,.35);
  }
  .card--back { left: 45px; }
  .card--front { left: 615px; background: var(--paper); }

  .back-art {
    position: absolute;
    inset: 0;
    background: linear-gradient(155deg, var(--orange) 0%, var(--orange) 35%, var(--copper) 75%, var(--olive) 100%);
  }

  .wordmark {
    position: absolute;
    display: flex;
    align-items: center;
    font-family: "Montserrat", sans-serif;
    font-weight: 400;
    letter-spacing: .18em;
    text-transform: uppercase;
    white-space: nowrap;
  }
  .wordmark__dot { flex: none; border-radius: 50%; }

  .card--back .wordmark {
    left: 50%; top: 50%;
    transform: translate(-50%, -50%);
    gap: 16px;
    color: var(--paper);
    font-size: 22px;
  }
  .card--back .wordmark__dot {
    width: 52px; height: 52px;
    border: 2px solid var(--paper);
  }

  .card--front .wordmark {
    left: 22px; top: 132px;
    width: 240px;
    flex-direction: column;
    gap: 14px;
    color: var(--ink);
    font-size: 14px;
    letter-spacing: .16em;
  }
  .card--front .wordmark__dot {
    width: 68px; height: 68px;
    background: var(--orange);
  }

  .divider {
    position: absolute;
    left: 276px; top: 66px;
    display: flex;
    flex-direction: column;
    gap: 14px;
  }
  .divider__seg { width: 1.5px; background: var(--rule); }
  .divider__seg--top { height: 38px; }
  .divider__seg--mid { height: 72px; width: 2px; background: var(--orange); }
  .divider__seg--bottom { height: 38px; }

  .contact {
    position: absolute;
    left: 300px; top: 74px;
    color: var(--ink);
  }
  .contact__name {
    font-family: "Montserrat", sans-serif;
    font-weight: 700;
    font-size: 21px;
    line-height: 1.1;
    text-transform: uppercase;
  }
  .contact__role {
    font-size: 12.5px;
    font-weight: 400;
    margin: 3px 0 16px;
  }
  .contact__list { list-style: none; font-size: 12px; font-weight: 300; }
  .contact__list li {
    display: flex; align-items: center; gap: 8px;
    margin-bottom: 6px;
  }
  .contact__icon { width: 11px; height: 11px; flex: none; fill: var(--orange); }
</style>
</head>
<body>

<section class="card card--back" aria-label="Card back">
  <div class="back-art" role="img" aria-label="Decorative landscape artwork in orange, copper and olive tones"></div>
  <div class="wordmark">
    <span class="wordmark__dot"></span>
    <span class="wordmark__name">Copper Lane Pictures</span>
  </div>
</section>

<section class="card card--front" aria-label="Card front">
  <div class="wordmark">
    <span class="wordmark__dot"></span>
    <span class="wordmark__name">Copper Lane Pictures</span>
  </div>

  <div class="divider" aria-hidden="true">
    <span class="divider__seg divider__seg--top"></span>
    <span class="divider__seg divider__seg--mid"></span>
    <span class="divider__seg divider__seg--bottom"></span>
  </div>

  <div class="contact">
    <h1 class="contact__name">Dale Morrow</h1>
    <p class="contact__role">Cinematographer-Director</p>
    <ul class="contact__list">
      <li>
        <svg class="contact__icon" viewBox="0 0 24 24" aria-hidden="true"><path d="M6.6 10.8a15.1 15.1 0 0 0 6.6 6.6l2.2-2.2c.3-.3.7-.4 1-.2 1.1.4 2.3.6 3.6.6.6 0 1 .4 1 1V20c0 .6-.4 1-1 1A17 17 0 0 1 3 4c0-.6.4-1 1-1h3.5c.6 0 1 .4 1 1 0 1.3.2 2.5.6 3.6.1.3 0 .7-.2 1z"/></svg>
        <span>0491 570 158</span>
      </li>
      <li>
        <svg class="contact__icon" viewBox="0 0 24 24" aria-hidden="true"><path d="M2 5h20v14H2z M2 5l10 8 10-8" stroke="#fff" stroke-width="1.6"/></svg>
        <span>mail@copperlanepix.com.au</span>
      </li>
      <li>
        <svg class="contact__icon" viewBox="0 0 24 24" aria-hidden="true"><circle cx="12" cy="12" r="10"/><path d="M2 12h20M12 2c3 3 3 17 0 20M12 2c-3 3-3 17 0 20" stroke="#fff" stroke-width="1.4" fill="none"/></svg>
        <span>www.copperlanepix.com.au</span>
      </li>
    </ul>
  </div>
</section>

</body>
</html>
```